New Law Firm needs a business card design

I need a business card for my new law firm called Tansey Wills and Probate. I would like designs to use my logo attached. My firm is new and modern. I like the colors orange, white, grey and black. The design I will chose will be one which uses color well, one which looks impressive, smart and modern.

Target Market(s)

Adults aged 30 to 50 seeking professional advice.

Industry/Entity Type

Law Firm

Requirements
Must have
• My logo which is attached.

Must have a modern font, similar to my logo and draft business card.
Should not have
• Any symbols about law, such as scales etc.

```html
<!DOCTYPE html>
<html lang="en">
<head>
<meta charset="utf-8">
<title>Tansey Wills &amp; Probate — Business Card</title>
<link rel="stylesheet" href="https://fonts.googleapis.com/css2?family=Montserrat:wght@400&family=Roboto+Condensed:ital,wght@0,400;0,700;1,400&display=swap">
<style>
  :root {
    --backdrop: #a9a6a2;
    --paper: #ffffff;
    --charcoal: #3b3f43;
    --ink: #2a2c2e;
    --muted: #6d7074;
    --orange: #f0a12b;
  }
  * { box-sizing: border-box; margin: 0; padding: 0; }
  html, body { width: 1200px; height: 1044px; overflow: hidden; }
  body {
    background: var(--backdrop);
    font-family: "Roboto Condensed", sans-serif;
    position: relative;
  }
  .card {
    position: absolute;
    width: 520px;
    height: 298px;
    border-radius: 3px;
    overflow: hidden;
    box-shadow: 0 10px 28px rgba(0,0,0,0.18);
  }

  /* Front */
  .card--front { left: 70px; top: 560px; background: var(--paper); }
  .front__name {
    position: absolute; left: 34px; top: 30px;
    font-weight: 700; font-size: 22px; color: var(--ink);
  }
  .front__credentials {
    position: absolute; left: 34px; top: 62px;
    font-style: italic; font-size: 15px; line-height: 1.3; color: var(--muted);
  }
  .front__contacts {
    position: absolute; left: 34px; top: 142px;
    list-style: none; font-size: 13px; color: var(--ink);
  }
  .front__contacts li { display: flex; align-items: center; gap: 10px; height: 20px; }
  .front__contacts li:first-child { font-weight: 700; }
  .front__contacts svg { width: 12px; height: 12px; fill: var(--charcoal); flex: none; }
  .front__band {
    position: absolute; left: 0; right: 0; bottom: 0; height: 16px;
    background: var(--charcoal);
  }

  /* Firm name in place of the mark */
  .firm-name {
    position: absolute;
    font-family: "Roboto Condensed", sans-serif;
    font-weight: 400;
    font-size: 20px;
    line-height: 1;
    white-space: nowrap;
    color: var(--muted);
  }
  .card--front .firm-name { right: 34px; bottom: 52px; }

  /* Back */
  .card--back { left: 600px; top: 170px; background: var(--charcoal); }
  .back__panel {
    position: absolute; left: 0; top: 0; width: 330px; height: 176px;
    background: var(--paper);
    border-radius: 0 0 90px 0;
  }
  .card--back .firm-name { left: 40px; top: 76px; }
  .back__rule {
    position: absolute; left: 250px; right: 0; top: 188px; height: 2px;
    background: var(--orange);
  }
  .back__services {
    position: absolute; left: 354px; top: 48px;
    list-style: none; font-family: "Montserrat", sans-serif;
    font-size: 15px; line-height: 1.45; color: var(--paper);
  }
  .back__services li::before { content: "•"; margin-right: 8px; }
  .back__notice {
    position: absolute; left: 26px; right: 20px; bottom: 70px;
    font-weight: 700; font-size: 14px; color: var(--paper);
  }
</style>
</head>
<body>

<section class="card card--front" aria-label="Business card front">
  <h1 class="front__name">Daniel Marsh</h1>
  <p class="front__credentials">Lawyer<br>Assoc.Deg.Law, BLJSt, LLB,<br>Grad Dip Law.</p>
  <ul class="front__contacts">
    <li><svg viewBox="0 0 12 12"><path d="M6 0a4 4 0 0 0-4 4c0 3 4 8 4 8s4-5 4-8a4 4 0 0 0-4-4zm0 5.5A1.5 1.5 0 1 1 6 2.5a1.5 1.5 0 0 1 0 3z"/></svg>Your Communication Address of Office</li>
    <li><svg viewBox="0 0 12 12"><path d="M2.5 0.5l2 2.5-1 1.5c.8 1.6 2 2.8 3.5 3.5l1.5-1 2.5 2-1 2.5C5 11 1 7 0.5 2z"/></svg>00.00.00.000</li>
    <li><svg viewBox="0 0 12 12"><path d="M2 4h8v7H2zM3 1h6v2H3z"/></svg>00.00.00.000</li>
    <li><svg viewBox="0 0 12 12"><path d="M0 2h12v8H0zm1 1v.4l5 3.3 5-3.3V3z"/></svg>daniel@tanseyprobate.com.au</li>
  </ul>
  <p class="firm-name">Tansey Wills &amp; Probate</p>
  <div class="front__band"></div>
</section>

<section class="card card--back" aria-label="Business card back">
  <div class="back__panel"></div>
  <p class="firm-name">Tansey Wills &amp; Probate</p>
  <ul class="back__services">
    <li>Wills</li>
    <li>Powers of Attorney</li>
    <li>Deceased Estates</li>
    <li>Will Disputes</li>
  </ul>
  <div class="back__rule"></div>
  <p class="back__notice">Liability limited by a scheme approved under professional standards legislation.</p>
</section>

</body>
</html>
```